BrightFold Partners Advisory needs business cards

BrightFold Partners Advisory is a new approach to consulting: we believe in partnering our clients in a hands-on, side-by-side, rolling-up-our sleeves approach, rather than being removed and aloof consultants.

We have a logo design developped through PixelHarbor (see attachment) and need to move to the stage of designing a business card for our 7 founding members.

Target Market(s)

Senior executives in local and global companies (such as Fizzmont Soda, Parvanta, Dorvik, etc)

Industry/Entity Type

Business

Requirements
Must have
• Look and feel: The design reflect the logo: i.e. professional, modern and approachable (as opposed to corporate traditional and remote). We are looking for a high quality, premium design.

Content must haves:
- prominent: our logo, person's name, function, phone number and e-mail address
- less prominent: company address and website

Example: BrightFold Partners Advisory logo, Maren Vollers, Partner, +44 (0)782 307 5918, maren_vollers@brightfoldpartners.example / 17 Harrowgate Lane, Esher, Surrey, UK, KT10 3PW - www.brightfoldpartners.example

- Both sides of the card can be used
- Both versions of the logo can be used (on black or on white)

```html
<!DOCTYPE html>
<html lang="en">
<head>
<meta charset="utf-8">
<title>BrightFold Partners Advisory – Business Card</title>
<link rel="stylesheet" href="https://fonts.googleapis.com/css2?family=Saira:wght@400;500&display=swap">
<style>
  :root {
    --backdrop: #3b3b3b;
    --teal-deep: #033f4c;
    --teal-mid: #0a7d98;
    --teal-bright: #1fb6e0;
    --band-dark: #3f6670;
    --band-mid: #5f8e99;
    --band-glow: #7fc8de;
    --brand-blue: #1ea3dc;
    --ink-dark: #1f1f1f;
    --ink-light: #ffffff;
    --ink-soft: #e3eef1;
    --paper: #ffffff;
  }
  * { margin: 0; padding: 0; box-sizing: border-box; }
  html, body { width: 1200px; height: 900px; overflow: hidden; }
  body {
    background: var(--backdrop);
    font-family: "Saira", Arial, sans-serif;
    position: relative;
  }
  .card {
    position: absolute;
    top: 300px;
    width: 525px;
    height: 300px;
    overflow: hidden;
  }

  /* Front */
  .card-front {
    left: 58px;
    background: radial-gradient(ellipse 70% 80% at 45% 30%, var(--teal-bright) 0%, var(--teal-mid) 45%, var(--teal-deep) 100%);
  }
  .brand-mark {
    position: absolute;
    border-radius: 50%;
    background: var(--brand-blue);
  }
  .card-front .brand-mark { left: 112px; top: 94px; width: 106px; height: 106px; }
  .brand-name {
    position: absolute;
    font-weight: 500;
    line-height: 1.05;
    letter-spacing: -0.5px;
    white-space: nowrap;
  }
  .card-front .brand-name { left: 232px; top: 118px; font-size: 27px; color: var(--ink-light); }
  .front-web {
    position: absolute; left: 0; width: 100%; top: 227px;
    text-align: center; color: var(--ink-light);
    font-size: 15px; letter-spacing: 1.4px;
  }
  .front-address {
    position: absolute; left: 0; width: 100%; top: 248px;
    text-align: center; color: var(--ink-soft);
    font-size: 11px; letter-spacing: 1.2px;
  }

  /* Back */
  .card-back { left: 617px; background: var(--paper); }
  .card-back .brand-mark { left: 52px; top: 30px; width: 88px; height: 88px; }
  .card-back .brand-name { left: 150px; top: 54px; font-size: 24px; color: var(--ink-dark); }
  .contact-band {
    position: absolute; left: 0; top: 145px; width: 100%; height: 138px;
    background:
      radial-gradient(ellipse 45% 60% at 55% 0%, var(--band-glow) 0%, rgba(127,200,222,0) 100%),
      linear-gradient(90deg, var(--band-dark) 0%, var(--band-mid) 50%, var(--band-dark) 100%);
    color: var(--ink-light);
  }
  .person-name { position: absolute; left: 41px; top: 25px; font-size: 17px; line-height: 20px; }
  .person-role { position: absolute; left: 41px; top: 44px; font-size: 13px; line-height: 16px; color: var(--ink-soft); }
  .person-address {
    position: absolute; left: 41px; top: 68px;
    font-size: 11.5px; line-height: 15px; color: var(--ink-soft);
  }
  .contact-list { position: absolute; left: 283px; top: 27px; right: 16px; list-style: none; }
  .contact-item {
    display: flex; align-items: center; gap: 9px;
    height: 16px; margin-bottom: 16.5px;
    font-size: 11.5px; white-space: nowrap;
  }
  .contact-icon { width: 16px; height: 16px; flex: none; }
</style>
</head>
<body>

  <section class="card card-front" aria-label="Card front">
    <div class="brand-mark"></div>
    <div class="brand-name">BrightFold<br>Partners Advisory</div>
    <p class="front-web">www.brightfoldpartners.example</p>
    <p class="front-address">17 Harrowgate Lane, Esher, UK, KT10 3PW</p>
  </section>

  <section class="card card-back" aria-label="Card back">
    <div class="brand-mark"></div>
    <div class="brand-name">BrightFold<br>Partners Advisory</div>

    <div class="contact-band">
      <p class="person-name">Tomas Varela Brandt</p>
      <p class="person-role">Partner</p>
      <p class="person-address">Av. Serra Clara 2180, Bl3, Apt 204,<br>Jardim Oceano, Rio de Janeiro,<br>CEP 22790-410</p>

      <ul class="contact-list">
        <li class="contact-item">
          <svg class="contact-icon" viewBox="0 0 16 16" aria-hidden="true"><rect x="4" y="1" width="8" height="14" rx="1.5" fill="none" stroke="#fff" stroke-width="1.4"/><circle cx="8" cy="12.5" r="0.9" fill="#fff"/></svg>
          <span>+(55) 21 9480 3316</span>
        </li>
        <li class="contact-item">
          <svg class="contact-icon" viewBox="0 0 16 16" aria-hidden="true"><rect x="1" y="3.5" width="14" height="9" fill="#fff"/><path d="M1 3.5 L8 9 L15 3.5" fill="none" stroke="#5f8e99" stroke-width="1.2"/></svg>
          <span>tomas@brightfoldpartners.example</span>
        </li>
        <li class="contact-item">
          <svg class="contact-icon" viewBox="0 0 16 16" aria-hidden="true"><circle cx="8" cy="8" r="6.8" fill="none" stroke="#fff" stroke-width="1.4"/><ellipse cx="8" cy="8" rx="3" ry="6.8" fill="none" stroke="#fff" stroke-width="1"/><line x1="1.2" y1="8" x2="14.8" y2="8" stroke="#fff" stroke-width="1"/></svg>
          <span>www.brightfoldpartners.example</span>
        </li>
      </ul>
    </div>
  </section>

</body>
</html>
```